依頼概要
〇依頼の目的/概要
電子書籍(lumora)の表紙デザインをおねがいします。

〇画像サイズ
表紙サイズの理想的な寸法は2560×1600ピクセルです。
注:画像の寸法は1000×625ピクセル以上であることが必要です。
画像の最大の寸法は10000×10000ピクセルです。

〇タイトル
夜更けの庭で青い灯をさがす旅の物語です!

〇帯キャッチ

・眠ることも許されない
死にたくなるようなかゆみと痛みから
柔らかい潤いのある肌になった

・人生の波と家族とのご縁をひもといて
薬を使わずに治す

・「絶対に治る、治ったら
同じように苦しんでいる人の為に役立つ本を書こう」
・・・と決めていました。

デザイナーさんの判断で、
どれかを使ってもらっても、
または全部を使ってもらってもOKです。

〇著者 ぽんたるべカフェ 占導師 千景(柴崎奈緒)

文字の大きさと配置と色のインパクトがあって一目惚れしました。
修正依頼にも迅速な対応もありがたかったです。

初めての電子書籍の執筆と初めてのワークベリーへの仕事依頼で、
ドキドキで、いろいろ小さなわからないところだらけでした。
たくさんの提案、どれも素敵なものばかりですべての提案者の方々に
感謝の氣持ちでいっぱいです。ありがとうございました。
これからもアトピー性皮膚炎を克服するための電子書籍を執筆していく予定なので
また、協力していただけたら嬉しいです。

```html
<!DOCTYPE html>
<html lang="ja">
<head>
<meta charset="utf-8">
<title>夜更けの庭で青い灯をさがす旅の物語です!</title>
<link rel="stylesheet" href="https://fonts.googleapis.com/css2?family=Noto+Sans+JP:wght@400;500;700;900&display=swap">
<style>
  :root {
    --ink: #1a1a1a;
    --soft-ink: #333333;
    --paper: #ffffff;
    --accent: #e5484f;
    --band: #f8d3d1;
    --frame: #e9dede;
    --art-light: #fdf0d6;
    --art-deep: #f6c670;
    --photo-light: #e8e1dc;
    --photo-deep: #b9a79c;
  }
  * { margin: 0; padding: 0; box-sizing: border-box; }
  html, body { width: 802px; height: 1200px; overflow: hidden; background: var(--paper); }
  body { font-family: "Noto Sans JP", sans-serif; color: var(--ink); }
  .cover {
    position: relative;
    width: 802px;
    height: 1200px;
    background: var(--paper);
    border: 3px solid var(--frame);
    overflow: hidden;
  }
  .title {
    position: absolute;
    left: 36px;
    top: 30px;
    width: 740px;
    font-weight: 900;
    font-size: 90px;
    line-height: 110px;
    letter-spacing: 2px;
    white-space: nowrap;
  }
  .author {
    position: absolute;
    left: 40px;
    top: 410px;
    font-size: 26px;
    font-weight: 500;
    white-space: nowrap;
  }
  .mascot-art {
    position: absolute;
    left: 500px;
    top: 462px;
    width: 210px;
    height: 170px;
    background: linear-gradient(160deg, var(--art-light), var(--art-deep));
  }
  .message {
    position: absolute;
    left: 40px;
    top: 648px;
    color: var(--accent);
    font-weight: 500;
    font-size: 44px;
    line-height: 56px;
    white-space: nowrap;
  }
  .message strong {
    display: block;
    font-size: 60px;
    font-weight: 900;
    line-height: 80px;
  }
  .band {
    position: absolute;
    left: 0;
    top: 858px;
    width: 100%;
    height: 342px;
    background: var(--band);
  }
  .band-lead {
    position: absolute;
    left: 52px;
    top: 22px;
    font-size: 25px;
    line-height: 38px;
    font-weight: 500;
    color: var(--soft-ink);
    white-space: nowrap;
  }
  .band-promise {
    position: absolute;
    left: 52px;
    top: 112px;
    font-size: 54px;
    font-weight: 900;
    line-height: 70px;
  }
  .band-resolve {
    position: absolute;
    left: 52px;
    top: 200px;
    font-size: 24px;
    line-height: 40px;
    font-weight: 500;
    color: var(--soft-ink);
    white-space: nowrap;
  }
  .author-photo {
    position: absolute;
    left: 605px;
    top: 122px;
    width: 170px;
    height: 196px;
    background: linear-gradient(160deg, var(--photo-light), var(--photo-deep));
  }
</style>
</head>
<body>
  <main class="cover">
    <h1 class="title">夜更けの庭で青い<br>灯をさがす旅の<br>物語です！</h1>
    <p class="author">ぽんたるべカフェ　占導師　千景(柴崎奈緒)　著</p>
    <div class="mascot-art" role="img" aria-label="ハートを抱きしめるキャラクターのイラスト"></div>
    <p class="message">人生の波と家族との<br>ご縁をひもといて<strong>薬を使わずに治す</strong></p>
    <section class="band">
      <p class="band-lead">眠ることも許されない死にたくなるようなかゆみと痛みから<br>柔らかい潤いのある肌になった。</p>
      <p class="band-promise">絶対に治る</p>
      <p class="band-resolve">治ったら同じように苦しんでいる人の為に<br>役立つ本を書こう！・・・と決めていました。</p>
      <div class="author-photo" role="img" aria-label="著者のポートレート写真"></div>
    </section>
  </main>
</body>
</html>
```